We need a cover designed for our book on parenting. The focus of this book is on the parents, not on the child! We like the idea of this title having a double meaning - insight as in gaining insights into parenting, and "in sight" as in looking inward as parents and how to improve ourselves rather than looking outward to improve our children. We would love for the cover to somehow represent this double meaning. I can upload an excerpt from the book soon over the next few days.
Updates

Reason: We are still reviewing the amazing designs! Thank you so much! :)

Target Market(s)

Parents with kids of any age from babies through adult children.

Requirements
Must have
• Title is: Steady Hearth Homes
• Subtitle is: Building Calm Households Daily
• Authors names: Tara Bellwin, LCSW Dorian Bellwin, Ph.D.

```html
<!DOCTYPE html>
<html lang="en">
<head>
<meta charset="utf-8">
<title>Steady Hearth Homes – Book Cover</title>
<link rel="stylesheet" href="https://fonts.googleapis.com/css2?family=Pinyon+Script&family=Roboto:wght@700&family=Alegreya+Sans:wght@400&family=Alegreya:wght@500&display=swap">
<style>
  :root {
    --page-bg: #f4f5f6;
    --cover-bg: #cfe3f2;
    --cover-bg-light: #dcebf6;
    --title-red: #a8111a;
    --rule-red: #9e1a22;
    --author-ink: #2a1616;
    --art-skin: #e8b9a2;
    --art-sky: #c3dbee;
  }
  * { margin: 0; padding: 0; box-sizing: border-box; }
  html, body {
    width: 960px;
    height: 1200px;
    overflow: hidden;
    background: var(--page-bg);
  }
  .canvas {
    position: relative;
    width: 960px;
    height: 1200px;
  }
  .cover {
    position: absolute;
    left: 130px;
    top: 30px;
    width: 700px;
    height: 1140px;
    background: linear-gradient(180deg, var(--cover-bg-light) 0%, var(--cover-bg) 100%);
    box-shadow: 0 18px 40px rgba(0,0,0,0.12);
    overflow: hidden;
  }
  .title-script {
    position: absolute;
    top: 130px;
    left: 0;
    width: 100%;
    text-align: center;
    font-family: "Pinyon Script", cursive;
    font-size: 104px;
    line-height: 1;
    color: var(--title-red);
  }
  .title-caps {
    position: absolute;
    top: 300px;
    left: 0;
    width: 100%;
    text-align: center;
    font-family: "Roboto", sans-serif;
    font-weight: 700;
    font-size: 128px;
    letter-spacing: 2px;
    line-height: 1;
    color: var(--title-red);
  }
  .subtitle-band {
    position: absolute;
    top: 500px;
    left: 0;
    width: 100%;
    height: 120px;
    border-top: 2px solid var(--rule-red);
    border-bottom: 2px solid var(--rule-red);
    display: flex;
    align-items: center;
    justify-content: center;
  }
  .subtitle {
    font-family: "Alegreya Sans", sans-serif;
    font-size: 42px;
    color: var(--title-red);
    letter-spacing: -0.5px;
  }
  .cover-art {
    position: absolute;
    top: 660px;
    left: 0;
    width: 520px;
    height: 330px;
    background: linear-gradient(100deg, var(--art-skin) 0%, #f0cdb9 45%, var(--art-sky) 100%);
    border-radius: 0 60px 60px 0;
    opacity: 0.85;
  }
  .authors {
    position: absolute;
    top: 1010px;
    left: 0;
    width: 100%;
    text-align: center;
    font-family: "Alegreya", serif;
    font-weight: 500;
    font-size: 48px;
    line-height: 1.3;
    color: var(--author-ink);
  }
</style>
</head>
<body>
  <main class="canvas">
    <section class="cover">
      <h1 class="title">
        <span class="title-script">Steady Hearth</span>
        <span class="title-caps">HOMES</span>
      </h1>
      <div class="subtitle-band">
        <p class="subtitle">Building Calm Households Daily</p>
      </div>
      <div class="cover-art" role="img" aria-label="An open hand reaching in from the left with a blue butterfly resting on the fingertips, among floating soap bubbles"></div>
      <div class="authors">
        <p class="author">Tara Bellwin, LCSW</p>
        <p class="author">Dorian Bellwin, Ph.&#8202;D.</p>
      </div>
    </section>
  </main>
</body>
</html>
```